Web Page for marketing online agency

We are an online marketing agency that is acing the direct response model. We engage with our customers throughout different marketing techniques as research copy-writing, advertisements and content writing. We would need a website design that will have four main aspects: The Vision; stating who we are, The Mission; stating what we do, The Team And It's Values, and a Contact Form. For this design we would want a sharp, clean and smart approach, with illustrated elements or suggestive images. You can use the attached copy, the logo, the USP and the motto. Please integrate them as you see fit while keeping in mind the previous needs and copy. This website is going to be our connection with our possible partners, future colleagues and even our clients. You may submit a design for one page or integrate the 4 different aspects on separate web pages.
Target Market(s)
business partners, future employees, age range 25-60
Industry/Entity Type
Direct Marketing
Number of Pages Required
1 page
Requirements
Must have
- Menu / Header
- 4 Parts or 4 Pages including: vision, mission, team, contact
- Logo
- Motto: Direct Brilliance
- USP: We help people help themselves.
- The copy attached
Nice to have
- Representative illustrated images or elements
Should not have
- A boring design, classical design - WordPress like

```html
<!DOCTYPE html>
<html lang="en">
<head>
<meta charset="utf-8">
<title>Velora – Direct Brilliance</title>
<link href="https://fonts.googleapis.com/css2?family=Raleway:wght@300;400;500;600;700;800&display=swap" rel="stylesheet">
<style>
:root{
  --blue:#2fa9e0;
  --blue-dark:#1e8fc4;
  --ink:#1d1d1d;
  --text:#444;
  --muted:#8a8a8a;
  --light:#e6e6e6;
  --footer:#2f2f2f;
  --white:#fff;
}
*{margin:0;padding:0;box-sizing:border-box}
html,body{width:1200px;height:3614px;overflow:hidden}
body{position:relative;background:var(--white);font-family:'Raleway',sans-serif;color:var(--text)}
.abs{position:absolute}
a{color:inherit;text-decoration:none}
.hl{color:var(--blue)}

/* header */
.site-header{top:0;left:0;width:1200px;height:89px;background:var(--white)}
.brand{left:241px;top:24px;display:flex;align-items:center;gap:10px}
.brand-name{font-weight:700;font-size:34px;color:var(--ink);letter-spacing:.5px}
.brand-dot{width:30px;height:30px;border-radius:50%;background:var(--blue)}
.nav{right:235px;top:38px;display:flex;gap:22px;font-size:14px;font-weight:500;color:#333;text-transform:uppercase}
.nav .active{color:var(--blue)}

/* hero */
.hero{top:89px;left:0;width:1200px;height:538px;background:linear-gradient(135deg,#d9d5d1 0%,#c9a996 45%,#e8e4e0 100%)}
.hero-title{left:236px;top:370px;background:var(--blue);color:#fff;font-size:40px;font-weight:600;padding:2px 12px;letter-spacing:.5px;line-height:1.2}
.hero-motto{left:284px;top:420px;background:rgba(30,30,30,.75);color:#fff;font-size:38px;font-weight:400;padding:0 14px;letter-spacing:1px;line-height:1.2}
.dots{left:574px;top:570px;display:flex;gap:8px}
.dots span{width:14px;height:14px;background:#111;border:2px solid #fff}
.dots span.on{background:var(--blue)}

/* section heads */
.sec-head{left:0;width:1200px;text-align:center}
.sec-num{font-size:72px;font-weight:300;color:#e2e2e2;line-height:1;position:absolute;left:488px;top:0}
.sec-kicker{position:relative;font-size:32px;color:var(--blue);font-weight:400;letter-spacing:.5px}
.sec-title{position:relative;font-size:34px;font-weight:800;color:var(--ink);line-height:1.1}
.sec-lead{position:relative;font-size:14px;font-weight:600;color:var(--ink);margin-top:14px;line-height:1.5}

/* vision */
.vision-photo-accent{left:104px;top:852px;width:140px;height:140px;background:var(--blue)}
.vision-photo-frame{left:100px;top:858px;width:450px;height:345px;background:var(--light)}
.vision-photo{left:114px;top:870px;width:436px;height:330px;background:linear-gradient(120deg,#5b6068 0%,#aeb4bb 50%,#e9ebee 100%);box-shadow:0 8px 14px rgba(0,0,0,.18)}
.vision-copy{left:578px;top:892px;width:580px;font-size:12.5px;line-height:1.5;color:#333}
.vision-copy p{margin-bottom:10px}

.values-row{left:278px;top:1270px;width:650px;display:flex;justify-content:space-between}
.value{width:100px;text-align:center;font-size:12px;color:var(--blue)}
.value svg{display:block;margin:0 auto 8px}
.values-line{left:280px;top:1404px;width:640px;height:1px;background:#ddd}
.values-line::before{content:"";position:absolute;left:0;top:-1px;width:95px;height:3px;background:var(--blue)}

/* mission */
.mission-band{left:0;top:1692px;width:1200px;height:236px;background:var(--blue)}
.mission-copy{left:236px;top:1716px;width:380px;color:#fff;font-size:12.5px;line-height:1.5}
.mission-copy ol{list-style:none;margin:12px 0}
.mission-copy li{margin-bottom:10px;display:flex;gap:10px}
.mission-copy li b.n{font-weight:800}
.mission-frame{left:680px;top:1651px;width:287px;height:314px;background:#e3e3e3}
.mission-photo{left:675px;top:1668px;width:280px;height:295px;background:linear-gradient(180deg,#dfe3e8 0%,#b4bcc6 60%,#3b4250 100%);box-shadow:0 6px 12px rgba(0,0,0,.2)}

/* team */
.member-accent{width:110px;height:8px;background:var(--blue)}
.member-frame{width:240px;height:255px;background:#e8e8e8}
.member-photo{width:232px;height:250px;box-shadow:0 6px 12px rgba(0,0,0,.2)}
.member-bio{width:540px;font-size:12px;line-height:1.5;color:#444}
.member-bio h3{font-size:13px;font-weight:700;color:var(--ink)}
.member-bio .role{color:var(--blue);margin-bottom:10px}
.member-bio p{margin-bottom:9px}

.team-values{left:330px;top:2844px;width:540px;display:grid;grid-template-columns:repeat(3,1fr);row-gap:16px}
.tv{text-align:center}
.tv-icon{width:70px;height:70px;margin:0 auto 6px;border-radius:50%;border:2px solid #d8eef9;display:flex;align-items:center;justify-content:center}
.tv h4{font-size:12px;font-weight:600;color:var(--blue)}
.tv p{font-size:10px;color:#555;line-height:1.35;margin-top:4px;padding:0 14px}

/* contact */
.contact{left:0;top:3193px;width:1200px;height:362px;background:linear-gradient(180deg,#3aaee3 0%,#2b9fd8 100%)}
.contact-title{left:0;top:3256px;width:1200px;text-align:center;color:#fff;font-size:26px;font-weight:700}
.field{border:2px solid #fff;color:#fff;font-size:12px;padding:9px 10px}
.submit{left:530px;top:3499px;width:145px;height:34px;border:2px solid #fff;color:#fff;font-weight:700;font-size:14px;letter-spacing:2px;text-align:center;line-height:30px}

/* footer */
.site-footer{left:0;top:3555px;width:1200px;height:59px;background:var(--footer);text-align:center;color:#bbb;font-size:10px}
.socials{display:flex;justify-content:center;gap:10px;padding-top:12px;margin-bottom:6px}
.socials span{width:10px;height:10px;border-radius:50%;background:#ddd}
.to-top{right:124px;top:3568px;width:32px;height:32px;border-radius:50%;background:var(--blue)}
</style>
</head>
<body>

<header class="abs site-header">
  <div class="abs brand"><span class="brand-name">Velora</span><span class="brand-dot"></span></div>
  <nav class="abs nav"><a class="active">Home</a><a>Our Vision</a><a>Our Mission</a><a>Our Team</a><a>Contact</a></nav>
</header>

<section class="abs hero" role="img" aria-label="Close-up photo of joined hands, a helping gesture"></section>
<h1 class="abs hero-title">WE HELP PEOPLE HELP THEMSELVES</h1>
<div class="abs hero-motto">VELORA - DIRECT BRILLIANCE</div>
<div class="abs dots"><span></span><span class="on"></span><span></span></div>

<!-- vision -->
<div class="abs sec-head" style="top:676px">
  <span class="sec-num">01</span>
  <div class="sec-kicker" style="padding-top:22px">OUR VISION</div>
  <h2 class="sec-title">WHO WE ARE?</h2>
  <p class="sec-lead">We are a direct response company that creates and sells information products and services that millions of people find<br>interesting and important in their lives.</p>
</div>

<div class="abs vision-photo-accent"></div>
<div class="abs vision-photo-frame"></div>
<div class="abs vision-photo" role="img" aria-label="Photo of business people shaking hands"></div>
<div class="abs vision-copy">
  <p>We are specialized in the self-reliance market and we serve conservative Americans.</p>
  <p>We are in this business to serve globally and to grow individually.<br>What we serve and inspire are people who need safety, comfort and peace of mind. We deliver <span class="hl">empowerment</span> through products that create fertile <span class="hl">shortcuts</span> to solutions, <span class="hl">disentangle</span> reality, <span class="hl">simplify</span> choices and ultimately <span class="hl">make lives better</span>. We give <span class="hl">reassurance</span> and <span class="hl">confidence</span> to these people through fresh, unique solutions.</p>
  <p>We get our <span class="hl">inspiration</span> from <span class="hl">modern heroes</span> and make their stories available for others.</p>
  <p>In a way we are <span class="hl">democratizing wisdom</span> because we solve serious problems shared by millions of people worldwide. We might not directly save lives, but we try to make a change. We help people help themselves.</p>
  <p>With our thirst for knowledge and drive for constant improvement, we know we'll find a solution to any challenge. And while doing that,<br>we decided <span class="hl">to solve our inner issues and harvest the best of our humanity</span>. We invest time and energy in becoming better <span class="hl">in the competition with ourselves</span>. We believe that <span class="hl">our better selves of tomorrow will nurture better tomorrows for others</span>.</p>
</div>

<div class="abs values-row">
  <div class="value"><svg width="92" height="92" viewBox="0 0 92 92"><circle cx="46" cy="46" r="44" fill="none" stroke="#2fa9e0" stroke-width="2"/><path d="M24 50 L38 40 L54 40 L68 50 M38 50 L48 58 L58 50" fill="none" stroke="#2fa9e0" stroke-width="3" stroke-linecap="round"/></svg>Fairness</div>
  <div class="value"><svg width="92" height="92" viewBox="0 0 92 92"><circle cx="46" cy="46" r="44" fill="none" stroke="#2fa9e0" stroke-width="2"/><path d="M46 62 C28 48 30 32 40 32 C44 32 46 36 46 38 C46 36 48 32 52 32 C62 32 64 48 46 62Z" fill="#2fa9e0"/></svg>Caring</div>
  <div class="value"><svg width="92" height="92" viewBox="0 0 92 92"><circle cx="46" cy="46" r="44" fill="none" stroke="#2fa9e0" stroke-width="2"/><path d="M22 52 Q34 40 46 52 T70 52 M22 62 Q34 50 46 62 T70 62" fill="none" stroke="#2fa9e0" stroke-width="3"/></svg>Freedom</div>
  <div class="value"><svg width="92" height="92" viewBox="0 0 92 92"><circle cx="46" cy="46" r="44" fill="none" stroke="#2fa9e0" stroke-width="2"/><path d="M24 46 Q46 18 68 46Z" fill="#2fa9e0"/><path d="M46 46 V64 Q46 70 40 68" fill="none" stroke="#2fa9e0" stroke-width="3"/></svg>Safety</div>
  <div class="value"><svg width="92" height="92" viewBox="0 0 92 92"><circle cx="46" cy="46" r="44" fill="none" stroke="#2fa9e0" stroke-width="2"/><path d="M30 62 V42 Q30 36 36 36 L56 36 Q62 36 62 42 V62" fill="none" stroke="#2fa9e0" stroke-width="3"/><circle cx="46" cy="48" r="6" fill="#2fa9e0"/></svg>Unconditioned help</div>
</div>
<div class="abs values-line"></div>

<!-- mission -->
<div class="abs sec-head" style="top:1482px">
  <span class="sec-num">02</span>
  <div class="sec-kicker" style="padding-top:22px">OUR MISSION</div>
  <h2 class="sec-title">WHAT IS IT THAT WE DO?</h2>
  <p class="sec-lead">We live and breathe direct response marketing.</p>
</div>

<div class="abs mission-band"></div>
<div class="abs mission-copy">
  <p>We are masters of direct response marketing.<br>Our expertise is three folded:</p>
  <ol>
    <li><b class="n">01</b><span>We create and aggregate great <b>information products.</b></span></li>
    <li><b class="n">02</b><span>We write content that <b>compels people to act.</b></span></li>
    <li><b class="n">03</b><span>We do <b>deep research</b> to offer simple, quick and easy solutions to people's most serious problems.</span></li>
  </ol>
  <p>We create content and build solutions to profound challenges for millions of people.</p>
</div>
<div class="abs mission-frame"></div>
<div class="abs mission-photo" role="img" aria-label="Portrait photo of a smiling businessman in a suit"></div>

<!-- team -->
<div class="abs sec-head" style="top:2022px">
  <span class="sec-num">03</span>
  <div class="sec-kicker" style="padding-top:22px">OUR TEAM</div>
  <h2 class="sec-title">&amp; VALUES</h2>
  <p class="sec-lead" style="margin-top:8px">We're a small team of smart, funny hard-working specialists who are pushing to become the #1 company in self-reliance. High ambition,<br>radical honesty and a result-oriented mindset are encouraged at Velora.</p>
</div>

<div class="abs member-accent" style="left:236px;top:2222px"></div>
<div class="abs member-frame" style="left:236px;top:2226px"></div>
<div class="abs member-photo" style="left:244px;top:2230px;background:linear-gradient(160deg,#cfd6de 0%,#8a8f96 55%,#2e2f33 100%)" role="img" aria-label="Portrait photo of the CEO"></div>
<div class="abs member-bio" style="left:494px;top:2244px">
  <h3>Dorin Velo</h3>
  <div class="role">CEO Velora</div>
  <p>Dorin started or was involved in 15 failed businesses before discovering online copywriting. After that, he ended up writing for Harbor Inc and did 10-12 "successful" projects there, at least 3 of which broke the million-dollar mark. He wrote the famous HearthVolt and the infamous CoilCode and Brennan Motor sales letters.</p>
  <p>In 2012 Dorin decided to start his own business, and to sell legit products. He and his team could actually be proud of. Six months into the business they had Greenyard</p>
  <p>Freedom, a legendary aquaponics/survival food offer that did over 150,000 initial sales. Ever since, they've been doing successful survival offers, and are one of the few "survival" players constantly coming up with new offers.</p>
  <p>Key personal strengths: copywriting, consulting, positioning, idea generation, mentoring.</p>
</div>

<div class="abs member-accent" style="left:236px;top:2518px"></div>
<div class="abs member-frame" style="left:236px;top:2522px"></div>
<div class="abs member-photo" style="left:244px;top:2526px;background:linear-gradient(160deg,#6b4b32 0%,#3a2a1f 55%,#1c1713 100%)" role="img" aria-label="Portrait photo of the cofounder"></div>
<div class="abs member-bio" style="left:494px;top:2534px">
  <h3>Matei Velo</h3>
  <div class="role">Cofounder &amp; Affiliate Manager Velora</div>
  <p>Strengths: strong networking skills, sales, risk management, leadership.</p>
  <p>Since the company's late 2012 start, Matei grew a network of <span class="hl">1000 affiliates</span>, that dominates OfferGrid's survival niche – <span class="hl">3 out of top 5 products</span> are Velora offers, under the Stillwater Prep brand.</p>
  <p>He currently oversees sales of <span class="hl">$10 million / year</span>, management of a <span class="hl">1M+</span> email list, marketing, business development and human resources for both the local Velora team and the international one.</p>
</div>

<div class="abs team-values">
  <div class="tv"><div class="tv-icon"><svg width="36" height="36" viewBox="0 0 36 36"><path d="M4 30 L14 20 L20 25 L32 8" fill="none" stroke="#2fa9e0" stroke-width="3"/><path d="M26 8 H32 V14" fill="none" stroke="#2fa9e0" stroke-width="3"/></svg></div><h4>Impact</h4><p>leverage, maximum results, 80-20, greatness</p></div>
  <div class="tv"><div class="tv-icon"><svg width="36" height="36" viewBox="0 0 36 36"><circle cx="18" cy="15" r="9" fill="none" stroke="#2fa9e0" stroke-width="3"/><path d="M13 27 H23 M14 32 H22" stroke="#2fa9e0" stroke-width="3"/></svg></div><h4>Wisdom</h4><p>learning mode 'on', practice of self-improvement as a lifestyle</p></div>
  <div class="tv"><div class="tv-icon"><svg width="36" height="36" viewBox="0 0 36 36"><circle cx="11" cy="12" r="5" fill="#2fa9e0"/><circle cx="25" cy="12" r="5" fill="#2fa9e0"/><path d="M3 30 Q11 18 18 30 Q25 18 33 30" fill="none" stroke="#2fa9e0" stroke-width="3"/></svg></div><h4>Team spirit</h4><p>cooperation and complementarity, synergy, 1+1 &gt; 2</p></div>
  <div class="tv"><div class="tv-icon"><svg width="36" height="36" viewBox="0 0 36 36"><circle cx="18" cy="10" r="5" fill="#2fa9e0"/><path d="M18 16 V26 M10 20 H26 M18 26 L12 34 M18 26 L24 34" stroke="#2fa9e0" stroke-width="3" fill="none"/></svg></div><h4>Courage</h4><p>feel the fear and do it anyway</p></div>
  <div class="tv"><div class="tv-icon"><svg width="36" height="36" viewBox="0 0 36 36"><circle cx="18" cy="18" r="12" fill="none" stroke="#2fa9e0" stroke-width="3"/><path d="M18 10 V18 L24 22" stroke="#2fa9e0" stroke-width="3" fill="none"/></svg></div><h4>Innovation mindset</h4><p>we recombine and reconnect things, so you can solve old problems in new, better ways</p></div>
  <div class="tv"><div class="tv-icon"><svg width="36" height="36" viewBox="0 0 36 36"><circle cx="18" cy="11" r="6" fill="#2fa9e0"/><path d="M6 33 Q18 14 30 33Z" fill="#2fa9e0"/></svg></div><h4>Ownership</h4><p>"leaders must own everything in their world. There is no one else to blame."</p></div>
</div>

<!-- contact -->
<section class="abs contact" role="img" aria-label="Blue band with a faint world map"></section>
<h2 class="abs contact-title">CONTACT US</h2>
<div class="abs field" style="left:234px;top:3306px;width:231px;height:34px">Full name</div>
<div class="abs field" style="left:482px;top:3306px;width:234px;height:34px">E-mail address</div>
<div class="abs field" style="left:735px;top:3306px;width:229px;height:34px">Website</div>
<div class="abs field" style="left:234px;top:3357px;width:730px;height:125px">Message</div>
<div class="abs submit">SUBMIT</div>

<footer class="abs site-footer">
  <div class="socials"><span></span><span></span><span></span></div>
  <div>Copyright Velora 2016. All Rights Reserved.</div>
</footer>
<div class="abs to-top"><svg width="32" height="32" viewBox="0 0 32 32"><path d="M10 19 L16 13 L22 19" fill="none" stroke="#fff" stroke-width="3"/></svg></div>

</body>
</html>
```